5th Battalion 42nd Cavalry Regiment " Grey Falcons"

Hello,
I am a lieutenant in the Northmark Defense Corps and my boss lieutenant colonel (commander) has asked me to come up with a business card for him. I threw a few designs toward him and he declined all of them. He really like the Knight business card background that is attached below(, but would like another Knight to replace it). We are 5th Battalion 42nd Cavalry Regiment (Grey Falcons is are Battalion Symbol) and are a Heavy Armored Combat team( Tanks and Carver's). He is an Infantry LTC would love a Bold but simple Grey Falcon riding on a horse. It doesn’t have to have the same back ground as the attached file named Finished Card, but will need all the information that is on both sides of the card. Thank you very much for your help and I look forward to seeing the designs.
V/R
Dale Whitcombe

Reason: My boss would like to see a few more designs.

```html
<!DOCTYPE html>
<html lang="en">
<head>
<meta charset="utf-8">
<title>5th Battalion 42nd Cavalry Regiment – Business Card</title>
<link href="https://fonts.googleapis.com/css2?family=PT+Sans:wght@400;700&display=swap" rel="stylesheet">
<style>
  :root {
    --page-bg: #2b2b2d;
    --card-white: #ffffff;
    --gold-dark: #7f7038;
    --gold-mid: #a8985a;
    --gold-light: #cfc28e;
    --olive-text: #7a7046;
    --ink: #26251c;
    --soft-tan: #d8cfae;
    --soft-tan-fade: rgba(216, 207, 174, 0);
    --edge-tone: #5f5d40;
  }
  * { margin: 0; padding: 0; box-sizing: border-box; }
  html, body {
    width: 1200px; height: 900px; overflow: hidden;
    background: var(--page-bg);
    font-family: "PT Sans", Verdana, sans-serif;
    color: var(--ink);
  }
  .sheet {
    position: relative; width: 1200px; height: 900px;
    display: flex; justify-content: center; align-items: center; gap: 30px;
  }
  .card {
    position: relative; width: 560px; height: 320px;
    background: var(--card-white);
    overflow: hidden;
    border: 3px solid var(--gold-mid);
    box-shadow: 0 10px 30px rgba(0,0,0,.45);
  }
  .card-edge {
    position: absolute; top: 0; bottom: 0; width: 10px;
    background: var(--edge-tone);
  }
  .card-edge--left { left: 0; }
  .card-edge--right { right: 0; }
  .horse-silhouette {
    position: absolute; left: 10px; top: 0; width: 230px; height: 200px;
    background: radial-gradient(ellipse at 35% 30%, var(--soft-tan) 0%, var(--soft-tan) 35%, var(--soft-tan-fade) 75%);
  }
  .unit-mark {
    position: absolute; display: flex; align-items: center; gap: 8px;
    font-weight: 700; font-size: 17px; color: var(--ink);
  }
  .unit-mark__dot {
    width: 14px; height: 14px; border-radius: 50%; background: var(--ink);
  }
  .gold-band {
    position: absolute;
    background: linear-gradient(180deg, var(--gold-light) 0%, var(--gold-mid) 45%, var(--gold-dark) 100%);
    box-shadow: 0 3px 6px rgba(0,0,0,.3);
  }

  /* Front */
  .front__title {
    position: absolute; right: 26px; top: 24px; text-align: right;
    color: var(--olive-text);
  }
  .front__regiment { font-size: 19px; }
  .front__nickname { font-size: 30px; font-weight: 700; margin-top: 2px; }
  .front__mark { left: 232px; top: 120px; }
  .contact {
    position: absolute; left: 30px; top: 150px;
    font-size: 12.5px; line-height: 1.45; color: #4a4838;
    list-style: none;
  }
  .contact__address { margin-top: 12px; font-size: 12.5px; }
  .front__band {
    right: 0; bottom: 34px; width: 270px; height: 66px;
    padding: 9px 18px; text-align: left;
  }
  .front__role {
    font-size: 16px; font-variant: small-caps; letter-spacing: .5px;
  }
  .front__name {
    font-size: 22px; font-weight: 700; letter-spacing: .5px;
  }

  /* Back */
  .back__title {
    position: absolute; left: 210px; top: 30px;
    font-size: 21px; color: var(--olive-text);
  }
  .back__mark { right: 34px; top: 82px; }
  .back__band {
    left: 0; top: 130px; width: 380px; height: 104px;
    padding: 12px 22px; text-align: center;
    font-size: 14px; line-height: 1.35; color: var(--ink);
  }
  .armor-scene {
    position: absolute; right: 10px; bottom: 0; width: 150px; height: 90px;
    background: linear-gradient(200deg, rgba(200,188,150,0) 0%, #cdc19a 55%, #a69a72 100%);
  }
</style>
</head>
<body>
<main class="sheet">

  <section class="card card--front" aria-label="Business card front">
    <div class="card-edge card-edge--left" role="img" aria-label="Camouflage pattern edge strip"></div>
    <div class="horse-silhouette" role="img" aria-label="Faint tan horse silhouette decoration"></div>

    <header class="front__title">
      <div class="front__regiment">5th Battalion, 42nd Cavalry Regiment</div>
      <div class="front__nickname">Grey Falcons</div>
    </header>

    <div class="unit-mark front__mark"><span class="unit-mark__dot"></span>Grey Falcons</div>

    <ul class="contact">
      <li>Work: 555-240-1835</li>
      <li>BB: 555-250-7416</li>
      <li>Cell: 555-720-3390</li>
      <li>martin.e.halvorsen@mail.example</li>
      <li class="contact__address">2318 Kestrel Ave., Fort Arden, KS 66000</li>
    </ul>

    <div class="gold-band front__band">
      <div class="front__role">Battalion Commander</div>
      <div class="front__name">MARTIN E. HALVORSEN</div>
    </div>
  </section>

  <section class="card card--back" aria-label="Business card back">
    <div class="card-edge card-edge--left" role="img" aria-label="Camouflage pattern edge strip"></div>
    <div class="horse-silhouette" role="img" aria-label="Faint tan horse silhouette decoration"></div>

    <h2 class="back__title">Grey Falcon Unit Vision</h2>

    <div class="unit-mark back__mark"><span class="unit-mark__dot"></span>Grey Falcons</div>

    <p class="gold-band back__band">
      A superbly fit, trained, disciplined, ready, and adaptable unit exercising mission command and teamwork to aggressively execute any mission and win!
    </p>

    <div class="armor-scene" role="img" aria-label="Sepia illustration of an armored vehicle"></div>
  </section>

</main>
</body>
</html>
```